Business Card Design with new logo

Dorian Pelleway 4172
E 118th St Ashwick, IL 62488
Cell: 217-555-0193
pellewayrestoration@mailvane.test

Classic Car Restoration Services Buy Sell Trade Consign

Dorian Pelleway 9698
Cell: 217-555-0193

```html
<!DOCTYPE html>
<html lang="en">
<head>
<meta charset="utf-8">
<title>Pelleway Restoration LLC – Business Card</title>
<link href="https://fonts.googleapis.com/css2?family=Questrial&display=swap" rel="stylesheet">
<style>
  :root {
    --backdrop: #1b1d21;
    --card: #fbfbfb;
    --navy: #1d3446;
    --red: #d0312d;
    --grey: #8a8d91;
    --white: #ffffff;
  }
  html, body {
    margin: 0;
    width: 1200px;
    height: 900px;
    overflow: hidden;
    background: var(--backdrop);
    font-family: "Questrial", "Century Gothic", sans-serif;
  }
  .card {
    position: absolute;
    left: 100px;
    top: 164px;
    width: 1000px;
    height: 572px;
    background: var(--card);
    border-radius: 40px;
    overflow: hidden;
  }
  .brand {
    position: absolute;
    left: 70px;
    top: 70px;
    display: flex;
    align-items: center;
    gap: 16px;
    color: var(--navy);
    font-size: 40px;
    letter-spacing: 1px;
  }
  .brand-dot {
    width: 30px;
    height: 30px;
    border-radius: 50%;
    background: var(--red);
  }
  .person {
    position: absolute;
    left: 70px;
    top: 190px;
  }
  .person-name {
    color: var(--red);
    font-size: 34px;
    font-weight: 400;
    letter-spacing: 0.5px;
    margin: 0;
  }
  .person-title {
    color: var(--grey);
    font-size: 22px;
    margin: 4px 0 22px;
  }
  .contact-line {
    display: flex;
    align-items: center;
    gap: 12px;
    color: var(--grey);
    font-size: 22px;
    margin-bottom: 8px;
  }
  .contact-icon {
    width: 20px;
    height: 20px;
    flex: none;
  }
  .address {
    position: absolute;
    right: 80px;
    top: 390px;
    color: var(--grey);
    font-size: 22px;
    font-style: normal;
    line-height: 1.3;
    text-align: left;
  }
  .band {
    position: absolute;
    left: 0;
    right: 0;
    top: 488px;
    height: 44px;
    display: flex;
  }
  .band-tagline {
    flex: 0 0 72%;
    background: var(--navy);
    color: var(--white);
    font-size: 21px;
    display: flex;
    align-items: center;
    padding-left: 50px;
    box-sizing: border-box;
    letter-spacing: 0.3px;
  }
  .band-accent {
    flex: 1;
    background: var(--red);
    display: flex;
    align-items: center;
    padding-left: 24px;
  }
  .band-accent-dot {
    width: 22px;
    height: 22px;
    border-radius: 50%;
    background: var(--white);
  }
</style>
</head>
<body>
  <main class="card">
    <div class="brand">
      <span class="brand-dot"></span>
      <span class="brand-name">PELLEWAY RESTORATION LLC</span>
    </div>

    <section class="person">
      <h1 class="person-name">MARLON TREADWELL</h1>
      <p class="person-title">Managing Director</p>
      <div class="contact-line">
        <svg class="contact-icon" viewBox="0 0 20 20" aria-hidden="true">
          <circle cx="10" cy="10" r="10" fill="#d0312d"/>
          <path d="M7 5.5l1.6 2.2-1 1.1a6 6 0 0 0 3.6 3.6l1.1-1 2.2 1.6-.9 1.6c-4 .2-8-3.8-7.8-7.8z" fill="#fff"/>
        </svg>
        <span>217-555-0193</span>
      </div>
      <div class="contact-line">
        <svg class="contact-icon" viewBox="0 0 20 20" aria-hidden="true">
          <circle cx="10" cy="10" r="10" fill="#d0312d"/>
          <rect x="5" y="6.5" width="10" height="7" fill="none" stroke="#fff" stroke-width="1.3"/>
          <path d="M5 6.5l5 4 5-4" fill="none" stroke="#fff" stroke-width="1.3"/>
        </svg>
        <span>pellewayrestoration@mailvane.test</span>
      </div>
    </section>

    <address class="address">
      Dorian Pelleway 4172<br>
      E 118th St Ashwick, IL 62488
    </address>

    <div class="band">
      <div class="band-tagline">Classic Car Restoration Services Buy Sell Trade Consign</div>
      <div class="band-accent"><span class="band-accent-dot"></span></div>
    </div>
  </main>
</body>
</html>
```